Recruitment talent email to send employers

We are a recruitment company specialising in STEM talent. We're after an eye catching email design to send our clients (ie employers) information about our top cadidates.

Target Market(s)

Employers

Requirements
Must have
• Must be clean/fresh looking, professional and concise

```html
<!DOCTYPE html>
<html lang="en">
<head>
<meta charset="utf-8">
<title>Nexa Group Talent Solutions – Top Candidates</title>
<link rel="stylesheet" href="https://fonts.googleapis.com/css2?family=Montserrat:ital,wght@0,400;0,500;0,600;0,700;0,800;1,400&family=Raleway:ital,wght@0,400;0,500;1,400&display=swap">
<style>
:root{
  --orange:#e87722;
  --orange-dark:#d96a17;
  --ink:#1f1f1f;
  --text:#333333;
  --muted:#555555;
  --footer:#2c2c2c;
  --btn:#2a2a2a;
  --white:#ffffff;
  --line:#d8d8d8;
  --avatar:#d9d9d9;
}
*{box-sizing:border-box;margin:0;padding:0}
html,body{width:1200px;height:4186px;overflow:hidden}
body{position:relative;background:var(--white);font-family:"Montserrat",Arial,sans-serif;color:var(--text)}
.abs{position:absolute}
.center{left:0;width:1200px;text-align:center}

/* Header */
.header{position:absolute;left:0;top:0;width:1200px;height:162px;background:var(--orange)}
.brand{position:absolute;left:122px;top:40px;display:flex;align-items:center;color:var(--white)}
.brand-name{font-weight:700;font-size:40px;line-height:1;letter-spacing:1px}
.brand-divider{width:3px;height:84px;background:var(--white);margin:0 28px}
.brand-tag{font-weight:500;font-size:34px;line-height:1.05;letter-spacing:1px}
.brand-tag small{display:block;font-size:15px;letter-spacing:2px;margin-top:6px}
.follow{position:absolute;right:38px;top:54px;display:flex;align-items:center;gap:12px;color:var(--white);font-size:24px;font-weight:500}
.follow .label{margin-right:10px}
.social-dot{width:44px;height:44px;border-radius:50%;background:var(--white)}

/* Hero */
.hero{position:absolute;left:0;top:162px;width:1200px;height:720px;background:linear-gradient(160deg,#4a3f36 0%,#2e2925 45%,#1d1b1a 100%)}
.hero-text{position:absolute;left:0;top:232px;width:1200px;text-align:center}
.hero-kicker{color:var(--orange);font-weight:500;font-size:44px;line-height:52px;letter-spacing:1px}
.hero-title{color:var(--white);font-weight:700;font-size:58px;line-height:70px;letter-spacing:1px;margin-top:4px}
.hero-rule{width:136px;height:4px;background:var(--orange);margin:28px auto 0}
.diamond{position:absolute;width:34px;height:34px;transform:rotate(45deg);border:5px solid var(--white)}
.diamond.orange{background:var(--orange)}
.diamond.dark{background:var(--btn)}

/* Intro */
.intro-lead{position:absolute;left:130px;top:960px;width:940px;text-align:center;font-weight:700;font-size:29px;line-height:38px;color:var(--ink)}
.intro-body{position:absolute;left:122px;top:1138px;width:510px;font-family:"Raleway",Arial,sans-serif;font-size:20px;line-height:26px;color:var(--text)}
.intro-photo{position:absolute;left:678px;top:1138px;width:324px;height:250px;background:var(--white);padding:10px;box-shadow:0 2px 14px rgba(0,0,0,.18)}
.intro-photo div{width:100%;height:100%;background:linear-gradient(135deg,#8a8f96 0%,#c8c8c8 50%,#3d3f44 100%)}

/* Candidates */
.candidates{position:absolute;left:0;top:1482px;width:1200px;height:1149px;background:var(--orange)}
.section-title{font-size:46px;font-weight:500;letter-spacing:1px;color:var(--ink)}
.section-title strong{font-weight:700}
.candidates .section-title strong{color:var(--white)}
.card{position:absolute;width:296px;height:276px;background:var(--white);text-align:center}
.avatar{position:absolute;left:70px;top:-86px;width:156px;height:156px;border-radius:50%;background:var(--avatar);border:8px solid #efefef;box-shadow:0 0 0 2px #e2e2e2}
.card-name{margin-top:92px;color:var(--orange);font-weight:700;font-size:26px}
.card-role{font-style:italic;font-size:15px;color:var(--muted);margin-top:4px}
.card-bio{font-family:"Raleway",Arial,sans-serif;font-style:italic;font-size:13px;line-height:17px;color:var(--muted);margin:10px 22px 0}
.btn-small{display:inline-block;margin-top:10px;width:118px;height:28px;line-height:28px;background:var(--btn);color:var(--white);font-size:12px;border-radius:4px}
.btn-large{position:absolute;left:502px;top:2493px;width:196px;height:56px;line-height:56px;background:var(--btn);color:var(--white);font-size:22px;text-align:center;border-radius:8px}

/* Why choose us */
.why .section-title strong{color:var(--orange)}
.stat{position:absolute;top:2840px;width:360px;text-align:center}
.stat-icon{height:60px}
.stat-num{color:var(--orange);font-weight:800;font-size:80px;line-height:84px;margin-top:10px}
.stat-label{font-weight:700;font-size:19px;color:var(--ink);margin-top:8px}
.stat-desc{font-family:"Raleway",Arial,sans-serif;font-size:18px;line-height:22px;color:var(--text);margin:10px auto 0;width:250px}
.stat-divider{position:absolute;top:2900px;width:2px;height:230px;background:var(--line)}

/* Partners */
.partners .section-title strong{color:var(--orange)}
.badge{position:absolute;width:120px;height:42px;background:#e6e6e6;border-radius:4px}

/* Footer */
.footer{position:absolute;left:0;top:3605px;width:1200px;height:581px;background:var(--footer);text-align:center;color:var(--white)}
.footer-title{position:absolute;left:0;top:68px;width:1200px;color:var(--orange);font-weight:700;font-size:46px;letter-spacing:1px}
.footer-text{position:absolute;left:0;top:196px;width:1200px;font-size:38px;line-height:53px;font-weight:500}
.footer-text b{color:var(--orange);font-weight:700}
.footer-follow{position:absolute;left:0;top:390px;width:1200px;font-size:22px;font-weight:500}
.footer-social{position:absolute;left:0;top:445px;width:1200px;display:flex;justify-content:center;gap:20px}
.footer-social .social-dot{background:var(--orange);width:50px;height:50px}
</style>
</head>
<body>

<header class="header">
  <div class="brand">
    <span class="brand-name">NEXA GROUP</span>
    <span class="brand-divider"></span>
    <span class="brand-tag">TALENT<br>SOLUTIONS<small>WORKFORCE DEVELOPMENT</small></span>
  </div>
  <div class="follow">
    <span class="label">Follow Us</span>
    <span class="social-dot" aria-label="Professional network"></span>
    <span class="social-dot" aria-label="Social page"></span>
    <span class="social-dot" aria-label="Microblog"></span>
  </div>
</header>

<section class="hero" role="img" aria-label="Photo of a smiling business team gathered around a laptop in a meeting">
  <div class="hero-text">
    <p class="hero-kicker">NEXA OFFERS BEST STEM<br>CANDIDATES CONNECT WITH</p>
    <h1 class="hero-title">LARGEST POOL OF<br>CANDIDATES IN LESSER TIME</h1>
    <div class="hero-rule"></div>
  </div>
</section>
<div class="diamond orange" style="left:583px;top:865px"></div>

<p class="intro-lead">With over 100 years in the recruitment business Nexa Group Recruitment Services is well positioned to help both Candidates and Employers to have an exceptional recruitment experience with us.</p>
<p class="intro-body">Our focus is in the area of white collar recruitment services, where we help businesses to find that one in a million candidate and candidates to find their ideal next step. Being Australia's premier membership organisation gives us access to some of Australia's top talent and by leveraging the broader services of Nexa Group we can ensure our hiring practices are second to none. We look forward to working with you!</p>
<div class="intro-photo"><div role="img" aria-label="Photo of two business people shaking hands"></div></div>

<section class="candidates">
  <h2 class="section-title abs center" style="top:96px">OUR <strong>TOP CANDIDATES</strong></h2>
</section>

<article class="card" style="left:120px;top:1747px"><div class="avatar" role="img" aria-label="Candidate photo placeholder"></div><p class="card-name">Candidate Name 1</p><p class="card-role">Designation</p><p class="card-bio">Lorem Ipsum is simply dummy text of the printing and typesetting industry. Lorem Ipsum has been the industry's standard dummy text</p><span class="btn-small">Read More</span></article>
<article class="card" style="left:452px;top:1747px"><div class="avatar" role="img" aria-label="Candidate photo placeholder"></div><p class="card-name">Candidate Name 2</p><p class="card-role">Designation</p><p class="card-bio">Lorem Ipsum is simply dummy text of the printing and typesetting industry. Lorem Ipsum has been the industry's standard dummy text</p><span class="btn-small">Read More</span></article>
<article class="card" style="left:785px;top:1747px"><div class="avatar" role="img" aria-label="Candidate photo placeholder"></div><p class="card-name">Candidate Name 3</p><p class="card-role">Designation</p><p class="card-bio">Lorem Ipsum is simply dummy text of the printing and typesetting industry. Lorem Ipsum has been the industry's standard dummy text</p><span class="btn-small">Read More</span></article>
<article class="card" style="left:120px;top:2157px"><div class="avatar" role="img" aria-label="Candidate photo placeholder"></div><p class="card-name">Candidate Name 4</p><p class="card-role">Designation</p><p class="card-bio">Lorem Ipsum is simply dummy text of the printing and typesetting industry. Lorem Ipsum has been the industry's standard dummy text</p><span class="btn-small">Read More</span></article>
<article class="card" style="left:452px;top:2157px"><div class="avatar" role="img" aria-label="Candidate photo placeholder"></div><p class="card-name">Candidate Name 5</p><p class="card-role">Designation</p><p class="card-bio">Lorem Ipsum is simply dummy text of the printing and typesetting industry. Lorem Ipsum has been the industry's standard dummy text</p><span class="btn-small">Read More</span></article>
<article class="card" style="left:785px;top:2157px"><div class="avatar" role="img" aria-label="Candidate photo placeholder"></div><p class="card-name">Candidate Name 6</p><p class="card-role">Designation</p><p class="card-bio">Lorem Ipsum is simply dummy text of the printing and typesetting industry. Lorem Ipsum has been the industry's standard dummy text</p><span class="btn-small">Read More</span></article>

<span class="btn-large">Read More</span>
<div class="diamond dark" style="left:583px;top:2614px"></div>

<section class="why">
  <h2 class="section-title abs center" style="top:2707px">WHY <strong>CHOOSE US?</strong></h2>

  <div class="stat" style="left:70px">
    <svg class="stat-icon" viewBox="0 0 60 60" width="60" height="60" aria-hidden="true"><g fill="none" stroke="#bdbdbd" stroke-width="2.5"><rect x="6" y="18" width="48" height="32" rx="3"/><path d="M22 18v-6h16v6M6 30h48M27 30v5h6v-5"/></g></svg>
    <p class="stat-num">200</p>
    <p class="stat-label">YEARS OF EXPERIENCE</p>
    <p class="stat-desc">Over 200 years of combined staff years of experience</p>
  </div>
  <div class="stat-divider" style="left:410px"></div>
  <div class="stat" style="left:420px">
    <svg class="stat-icon" viewBox="0 0 60 60" width="60" height="60" aria-hidden="true"><g fill="none" stroke="#bdbdbd" stroke-width="2.5"><circle cx="30" cy="18" r="10"/><path d="M12 54c0-12 8-20 18-20s18 8 18 20z"/></g></svg>
    <p class="stat-num">35,000</p>
    <p class="stat-label">CANDIDATES EMPLOYED</p>
    <p class="stat-desc">Over 35,000 candidates into great jobs</p>
  </div>
  <div class="stat-divider" style="left:776px"></div>
  <div class="stat" style="left:770px">
    <svg class="stat-icon" viewBox="0 0 60 60" width="60" height="60" aria-hidden="true"><g fill="none" stroke="#bdbdbd" stroke-width="2.5"><path d="M4 22l10-6 10 4 8-4 10 2 14 6M14 16l-6 16M46 18l6 14M20 34l8 8 6-2 8-8"/></g></svg>
    <p class="stat-num">1,700</p>
    <p class="stat-label">EMPLOYER PARTNERSHIPS</p>
    <p class="stat-desc">Over 1,700 Employers have partnered with us</p>
  </div>
</section>

<section class="partners">
  <h2 class="section-title abs center" style="top:3258px">OUR <strong>PARTNERS</strong></h2>
  <div class="badge" style="left:135px;top:3384px"></div>
  <div class="badge" style="left:298px;top:3384px"></div>
  <div class="badge" style="left:458px;top:3384px"></div>
  <div class="badge" style="left:625px;top:3384px"></div>
  <div class="badge" style="left:790px;top:3384px"></div>
  <div class="badge" style="left:958px;top:3384px"></div>
  <div class="badge" style="left:155px;top:3473px"></div>
  <div class="badge" style="left:350px;top:3473px"></div>
  <div class="badge" style="left:540px;top:3473px"></div>
  <div class="badge" style="left:738px;top:3473px"></div>
  <div class="badge" style="left:935px;top:3473px"></div>
</section>

<footer class="footer">
  <h2 class="footer-title">CONTACT US</h2>
  <p class="footer-text">Get in touch by ringing<br><b>1300 555 014</b> or by sending and email to<br><b>RECRUIT@NEXAGROUP.COM.AU</b></p>
  <p class="footer-follow">Follow Us</p>
  <div class="footer-social">
    <span class="social-dot" aria-label="Professional network"></span>
    <span class="social-dot" aria-label="Social page"></span>
    <span class="social-dot" aria-label="Microblog"></span>
  </div>
</footer>

</body>
</html>
```